Corvane spray foam and Environmental

I have business cards but need new ones. The ones I have are very bland. Here is. Y company website http://www.corvanesprayfoam.ca

Also I can send you copies of the current cards
I would also need my current logo on the new design as well.. Also spray foam and Environmental

Industry/Entity Type

Business

Logo Text

Corvane.

```html
<!DOCTYPE html>
<html lang="en">
<head>
<meta charset="utf-8">
<title>Corvane business card</title>
<link rel="stylesheet" href="https://fonts.googleapis.com/css2?family=Open+Sans:wght@600;700&family=Work+Sans:wght@400;500&display=swap">
<style>
:root{
  --bg:#e6e6e6;
  --ink:#3d3f4a;
  --purple:#5b2d7e;
  --grey-band:#b9b9b9;
  --white:#ffffff;
  --black:#000000;
  --line:#b8b8b8;
}
*{box-sizing:border-box;margin:0;padding:0}
html,body{width:1200px;height:800px;overflow:hidden;background:var(--bg)}
.canvas{position:relative;width:1200px;height:800px}
.card{position:absolute;left:310px;width:580px;height:338px;border-radius:26px;overflow:hidden;box-shadow:0 4px 10px rgba(0,0,0,.25)}
.card--front{top:40px;background:var(--white)}
.card--back{top:422px;background:var(--black)}
.brand{position:absolute;left:0;right:0;text-align:center}
.brand__mark{display:block;margin:0 auto;width:70px;height:58px}
.card--front .brand__mark{background:var(--ink)}
.card--back .brand__mark{background:var(--purple)}
.brand__name{display:block;margin-top:14px;font:700 29px/1 "Open Sans",sans-serif;letter-spacing:5px;padding-left:5px}
.card--front .brand__name{color:var(--ink)}
.card--back .brand__name{color:var(--white)}
.card--front .brand{top:45px}
.card--back .brand{top:22px}
.divider{position:absolute;left:294px;top:170px;width:2px;height:100px;background:var(--ink)}
.contact{position:absolute;top:180px;font-family:"Work Sans",sans-serif;color:var(--ink)}
.contact--left{right:304px;text-align:right}
.contact--right{left:320px;text-align:left}
.contact__title{font:500 18px/1 "Work Sans",sans-serif;letter-spacing:.5px;margin-bottom:10px}
.contact__row{display:flex;align-items:center;gap:8px;font-size:14px;line-height:20px}
.contact--left .contact__row{justify-content:flex-end}
.contact--left .contact__title{margin-right:12px}
.contact__icon{width:10px;height:10px;flex:none}
.address{position:absolute;left:0;bottom:0;width:580px;height:20px}
.address__band{position:absolute;left:0;top:0}
.address__text{position:absolute;left:120px;width:374px;bottom:2px;text-align:center;white-space:nowrap;color:var(--white);font:400 12.5px/16px "Work Sans",sans-serif;letter-spacing:.3px}
.services{position:absolute;left:0;top:150px;width:580px;height:170px}
.services__rule{position:absolute;left:0;width:580px;height:2px;background:var(--line)}
.services__split{position:absolute;left:290px;top:0;width:2px;height:170px;background:var(--line)}
.services__col{position:absolute;top:0;width:290px;text-align:center;color:var(--white)}
.services__col--foam{left:0}
.services__col--enviro{left:292px}
.services__head{height:40px;font:700 19px/42px "Open Sans",sans-serif;letter-spacing:4px}
.services__list{list-style:none;margin-top:10px;font:600 13.5px/17.6px "Open Sans",sans-serif;letter-spacing:1px}
</style>
</head>
<body>
<div class="canvas">

  <section class="card card--front">
    <div class="brand">
      <span class="brand__mark"></span>
      <span class="brand__name">CORVANE</span>
    </div>
    <div class="divider"></div>

    <div class="contact contact--left">
      <h2 class="contact__title">ENVIRONMENTAL</h2>
      <p class="contact__row">604-555-0182
        <svg class="contact__icon" viewBox="0 0 10 10"><path d="M2 1l2 2-1 1c.5 1.2 1.6 2.3 2.8 2.8l1-1 2 2-1.2 1.2C4.5 8.6 1.4 5.5 1 2.2z" fill="#5b2d7e"/></svg></p>
      <p class="contact__row">enviro1@corvanemail.ca
        <svg class="contact__icon" viewBox="0 0 10 10"><rect x=".8" y="2" width="8.4" height="6" fill="none" stroke="#5b2d7e" stroke-width="1.2"/><path d="M1 2.3l4 3 4-3" fill="none" stroke="#5b2d7e" stroke-width="1.1"/></svg></p>
      <p class="contact__row">www.corvanesprayfoam.ca
        <svg class="contact__icon" viewBox="0 0 10 10"><circle cx="5" cy="5" r="4" fill="none" stroke="#5b2d7e"/><ellipse cx="5" cy="5" rx="1.8" ry="4" fill="none" stroke="#5b2d7e" stroke-width=".8"/><path d="M1 5h8" stroke="#5b2d7e" stroke-width=".8"/></svg></p>
    </div>

    <div class="contact contact--right">
      <h2 class="contact__title">SPRAY FOAM</h2>
      <p class="contact__row"><svg class="contact__icon" viewBox="0 0 10 10"><path d="M2 1l2 2-1 1c.5 1.2 1.6 2.3 2.8 2.8l1-1 2 2-1.2 1.2C4.5 8.6 1.4 5.5 1 2.2z" fill="#5b2d7e"/></svg>604-555-0147</p>
      <p class="contact__row"><svg class="contact__icon" viewBox="0 0 10 10"><rect x=".8" y="2" width="8.4" height="6" fill="none" stroke="#5b2d7e" stroke-width="1.2"/><path d="M1 2.3l4 3 4-3" fill="none" stroke="#5b2d7e" stroke-width="1.1"/></svg>foam@corvanemail.ca</p>
      <p class="contact__row"><svg class="contact__icon" viewBox="0 0 10 10"><circle cx="5" cy="5" r="4" fill="none" stroke="#5b2d7e"/><ellipse cx="5" cy="5" rx="1.8" ry="4" fill="none" stroke="#5b2d7e" stroke-width=".8"/><path d="M1 5h8" stroke="#5b2d7e" stroke-width=".8"/></svg>www.corvanesprayfoam.ca</p>
    </div>

    <div class="address">
      <svg class="address__band" width="580" height="20" viewBox="0 0 580 20">
        <polygon points="0,0 98,0 110,20 0,20" fill="#5b2d7e"/>
        <polygon points="104,0 504,0 494,20 116,20" fill="#b9b9b9"/>
        <polygon points="510,0 580,0 580,20 500,20" fill="#5b2d7e"/>
      </svg>
      <p class="address__text">48 Larchmont Way Burnaby, British Columbia v5e 2k4, CA</p>
    </div>
  </section>

  <section class="card card--back">
    <div class="brand">
      <span class="brand__mark"></span>
      <span class="brand__name">CORVANE</span>
    </div>
    <div class="services">
      <div class="services__rule" style="top:0"></div>
      <div class="services__rule" style="top:40px"></div>
      <div class="services__rule" style="top:168px"></div>
      <div class="services__split"></div>
      <div class="services__col services__col--foam">
        <h3 class="services__head">SPRAY FROM</h3>
        <ul class="services__list">
          <li>ROOFING FOAM</li><li>SLABJACKING</li><li>2POUND/HALF POUND</li>
          <li>SOUND PROOFING</li><li>BATT INSULATION</li><li>ATTIC BLOW IN</li>
        </ul>
      </div>
      <div class="services__col services__col--enviro">
        <h3 class="services__head">ENVIRONMENTAL</h3>
        <ul class="services__list">
          <li>AIR MONITORING</li><li>ASBESTOS TESTING</li><li>ASBESTOS REMOVAL</li>
          <li>BUILDING DEMOLITION</li><li>LEAD TESTING</li><li>MOULD REMOVAL</li>
        </ul>
      </div>
    </div>
  </section>

</div>
</body>
</html>
```